Home care support

Design a a great and dynamic website for a healthcare business. Our business will be involved in providing care at home for people with disability and the elderly. Below is a link that I found for a company offering similar services in the US. I am looking for something like this .
I have my files - the latest project in here in through through Pixelmarket
Sample site : https://cedarbrookassistedliving.com/
Target Market(s)
people with disability and elderly seniors who need home care support
Industry/Entity Type
Health
Coding
Coded - Design and coding required
Number of Pages Required
5+ page
Requirements
Must have
- inspirational pictures and designed with the themed logo (files attached)
Nice to have
- This is my sample and should look like this : https://cedarbrookassistedliving.com/

```html
<!DOCTYPE html>
<html lang="en">
<head>
<meta charset="utf-8">
<title>Halvera Healthcare – Home Care</title>
<link rel="stylesheet" href="https://fonts.googleapis.com/css2?family=Raleway:wght@300;400;500;600;700&display=swap">
<style>
:root{
  --blue:#0c6fb6;
  --blue-bright:#0a9fdc;
  --blue-deep:#0868b0;
  --green:#74ab43;
  --green-dark:#5f9a33;
  --sky:#e4f3fb;
  --ink:#444a50;
  --muted:#6a7178;
  --line:#c9dde9;
  --grey:#8b8f93;
  --foot-bar:#eef3f6;
}
*{box-sizing:border-box;margin:0;padding:0}
html,body{width:1200px;height:4515px;overflow:hidden}
body{font-family:"Raleway",sans-serif;color:var(--ink);background:#fff;position:relative}
.abs{position:absolute}
.btn{position:absolute;display:flex;align-items:center;justify-content:center;border-radius:30px;font-weight:700;font-size:13px;letter-spacing:.3px;color:#fff;text-transform:uppercase}

/* top bar */
.topbar{left:0;top:0;width:1200px;height:35px;background:var(--green);color:#fff;font-size:12.5px;font-weight:500}
.social{position:absolute;top:7px;width:21px;height:21px;border-radius:50%;background:#fff}
.topbar .contact{position:absolute;top:10px;display:flex;align-items:center;gap:7px}

/* nav */
.nav{left:0;top:35px;width:1200px;height:91px;background:#fff;border-bottom:1px solid #e6eef3}
.brand{position:absolute;display:flex;align-items:center;gap:12px}
.brand .dot{width:58px;height:58px;border-radius:50%;background:var(--blue)}
.brand .name{font-size:34px;font-weight:700;color:var(--blue);letter-spacing:1px;line-height:1}
.menu{position:absolute;left:424px;top:38px;display:flex;font-size:13px;font-weight:500;color:#333}
.menu span{position:absolute;white-space:nowrap}
.menu .active{color:var(--blue)}
.menu .active::after{content:"";position:absolute;left:0;right:0;bottom:-9px;height:2px;background:var(--blue)}

/* hero */
.hero{left:0;top:126px;width:1200px;height:596px;background:var(--sky);overflow:hidden}
.hero h1{position:absolute;left:119px;top:140px;font-weight:300;font-size:38px;color:#7b8186;line-height:44px}
.hero h1 b{display:block;font-weight:600;color:var(--blue)}
.hero .lede{position:absolute;left:120px;top:242px;font-size:14px;line-height:24px;color:#555}
.hero .call{position:absolute;left:121px;top:308px;font-size:15px;font-weight:600;color:var(--green)}
.hero .call b{color:var(--blue);font-size:19px;font-weight:700}
.hero-photo{position:absolute;left:580px;top:-70px;width:1000px;height:1000px;border-radius:50%;background:linear-gradient(135deg,#c8d7c4 0%,#e9c7bf 50%,#6f8f74 100%)}
.hero-ring{position:absolute;left:566px;top:-84px;width:1028px;height:1028px;border-radius:50%;border:9px solid var(--blue-bright);border-right-color:transparent;border-bottom-color:transparent;transform:rotate(-30deg)}

/* about */
.about-photo{left:0;top:771px;width:605px;height:447px;background:radial-gradient(circle at 42% 50%,#c9c2bb 0%,#e8e4e0 38%,#fbfbfb 65%,#fff 80%)}
.section-title{font-weight:300;font-size:37px;line-height:1;letter-spacing:.3px}
.section-title b{font-weight:600}
.about h2{position:absolute;left:614px;top:838px;color:var(--green)}
.about h2 b{color:var(--blue)}
.rule{position:absolute;height:3px;width:56px}
.about p{position:absolute;left:614px;width:470px;font-size:15px;line-height:25px;color:#555}

/* care band */
.care{left:0;top:1293px;width:1200px;height:620px}
.care h2{position:absolute;left:0;width:1200px;top:62px;text-align:center;color:#fff}
.feature{position:absolute;color:#fff}
.feature h3{font-size:15px;font-weight:600;margin-bottom:6px}
.feature p{font-size:11.5px;line-height:17px;opacity:.95}
.feature.l{text-align:right;width:230px}
.ficon{position:absolute;width:80px;height:80px;border-radius:50%;border:3px solid #fff;display:flex;align-items:center;justify-content:center}

/* services */
.services h2{position:absolute;left:0;width:1200px;top:1965px;text-align:center;color:var(--green)}
.services h2 b{color:var(--blue)}
.card{position:absolute;width:236px;height:194px;border:2px solid var(--line);background:#fff;text-align:center}
.card svg{position:absolute;left:93px;top:28px}
.card h3{position:absolute;top:102px;width:100%;font-size:14px;font-weight:600;color:var(--blue)}
.card p{position:absolute;top:126px;left:24px;right:24px;font-size:10.5px;line-height:15px;color:var(--muted)}
.card.on{background:var(--green);border-color:var(--green)}
.card.on h3,.card.on p{color:#fff}

/* approach */
.approach-photo{left:0;top:2535px;width:605px;height:505px;background:linear-gradient(120deg,#8a6a3e 0%,#3c5a8c 45%,#d9b9a0 75%,#5a8a4a 100%)}
.approach{left:605px;top:2535px;width:595px;height:505px;background:var(--green);color:#fff}
.approach h2{position:absolute;left:84px;top:95px;font-size:26px;font-weight:400;line-height:37px}
.approach h2 b{font-weight:600}
.approach p{position:absolute;left:83px;top:200px;width:420px;font-size:13.5px;line-height:24px}

/* testimonials */
.quotes h2{position:absolute;left:0;width:1200px;top:3125px;text-align:center;color:var(--green)}
.quotes h2 b{color:var(--blue)}
.quote{position:absolute;top:3250px;width:419px;height:229px;border:2px solid var(--line);text-align:center}
.quote p{position:absolute;top:64px;left:36px;right:36px;font-size:14.5px;line-height:23px;color:#555}
.quote h4{position:absolute;top:176px;width:100%;font-size:14.5px;font-weight:600;color:#333}
.avatar{position:absolute;top:-46px;width:88px;height:88px;border-radius:50%;border:3px solid var(--green);background:radial-gradient(circle,#d8d2cc,#9e9790)}
.dots{position:absolute;left:560px;top:3514px;display:flex;gap:8px}
.dots i{width:13px;height:13px;border-radius:50%;border:1.5px solid #888;display:block}
.dots i.on{background:var(--blue);border-color:var(--blue)}

/* appointment */
.book{left:0;top:3560px;width:1200px;height:580px}
.book h2{position:absolute;left:0;width:1200px;top:120px;text-align:center;color:#fff;font-size:33px}
.book .sub{position:absolute;left:0;width:1200px;top:172px;text-align:center;color:#fff;font-size:17px;line-height:25px}
.book .sub b{font-weight:600}
.field{position:absolute;background:#fff;border-radius:3px;font-size:12.5px;color:#666;padding:13px 18px}

/* footer */
.foot-col{position:absolute;top:4228px;font-size:13px;line-height:25px;color:#6a6f74}
.foot-col h4{font-size:16px;font-weight:600;color:var(--blue);margin-bottom:12px;text-decoration:underline;text-underline-offset:5px;line-height:20px}
.foot-col .row{display:flex;align-items:center;gap:8px;color:#333;margin-bottom:10px}
.pin{width:22px;height:22px;border-radius:50%;background:var(--blue-bright);display:flex;align-items:center;justify-content:center}
.copy{left:0;top:4459px;width:1200px;height:56px;background:var(--foot-bar);text-align:center;font-size:12px;color:#6a6f74;line-height:56px}
</style>
</head>
<body>

<!-- top bar -->
<div class="abs topbar">
  <span class="social" style="left:128px"></span>
  <span class="social" style="left:155px"></span>
  <span class="social" style="left:182px"></span>
  <div class="contact" style="left:708px">
    <svg width="14" height="14" viewBox="0 0 24 24"><path fill="#fff" d="M6.6 10.8a15 15 0 0 0 6.6 6.6l2.2-2.2a1 1 0 0 1 1-.25 11.4 11.4 0 0 0 3.6.57 1 1 0 0 1 1 1V20a1 1 0 0 1-1 1A17 17 0 0 1 3 4a1 1 0 0 1 1-1h3.5a1 1 0 0 1 1 1c0 1.25.2 2.45.57 3.6a1 1 0 0 1-.25 1z"/></svg>
    (555) 014 2290
  </div>
  <div class="contact" style="left:866px">
    <svg width="16" height="12" viewBox="0 0 16 12"><rect x="0.5" y="0.5" width="15" height="11" fill="none" stroke="#fff"/><path d="M.5.5 8 7 15.5.5" fill="none" stroke="#fff"/></svg>
    hello@halverahealthcare.example
  </div>
</div>

<!-- nav -->
<header class="abs nav">
  <div class="brand" style="left:122px;top:16px"><span class="dot"></span><span class="name">HALVERA</span></div>
  <nav class="menu">
    <span class="active" style="left:0">HOME</span>
    <span style="left:102px">ABOUT US</span>
    <span style="left:231px">SERVICES</span>
    <span style="left:354px">RESOURCE</span>
    <span style="left:485px">BLOGS</span>
    <span style="left:590px">CONTACT</span>
  </nav>
</header>

<!-- hero -->
<section class="abs hero">
  <div class="hero-ring"></div>
  <div class="hero-photo" role="img" aria-label="Photo of a smiling nurse with a stethoscope holding hands with an elderly woman outdoors"></div>
  <h1>WELCOME TO<b>HALVERA HEALTHCARE</b></h1>
  <p class="lede">Lorem ipsum dolor sit amet, consectetur adipiscing elit,<br>sed do eiusmod tempor incididunt ut labore</p>
  <p class="call">For more Information: <b>Call Us (555) 014 2290</b></p>
  <span class="btn" style="left:114px;top:368px;width:236px;height:53px;background:var(--blue-bright)">Make an appointment</span>
</section>

<!-- about -->
<section class="about">
  <div class="abs about-photo" role="img" aria-label="Soft faded photo of an elderly man with a carer's hand on his shoulder"></div>
  <h2 class="section-title">ABOUT <b>HALVERA</b></h2>
  <span class="rule" style="left:614px;top:884px;background:var(--blue)"></span>
  <p style="top:912px">Lorem ipsum dolor sit amet, consectetur adipiscing elit, sed do eiusmod tempor incididunt ut labore</p>
  <p style="top:993px">voluptatem. Ut enim ad minima veniam, quis nostrum exercitationem ullam corporis suscipit laboriosam, nisi ut aliquid ex ea commodi consequatur? Quis autem vel eum iure reprehenderit qui in ea voluptate velit esse quam nihil molestiae consequatur, vel illum qui dolorem</p>
  <span class="btn" style="left:614px;top:1141px;width:168px;height:46px;background:var(--green)">Learn more</span>
</section>

<!-- care band -->
<section class="abs care">
  <svg class="abs" style="left:0;top:0" width="1200" height="620" viewBox="0 0 1200 620">
    <defs><linearGradient id="careGrad" x1="0" y1="0" x2="1" y2="0"><stop offset="0" stop-color="#0a6cb4"/><stop offset="1" stop-color="#05a6e0"/></linearGradient></defs>
    <path d="M0 0H1200V500Q900 600 600 602Q260 600 0 500Z" fill="url(#careGrad)"/>
    <path d="M110 548Q600 640 1100 548Q600 618 110 548Z" fill="#5cc3ec"/>
  </svg>
  <h2 class="section-title">PROVIDE BEST HOME <b>CARE SERVICE</b></h2>
  <span class="rule" style="left:572px;top:108px;background:#fff"></span>

  <div class="abs" style="left:420px;top:152px;width:380px;height:380px;border-radius:50%;background:rgba(255,255,255,.22)"></div>
  <div class="abs" style="left:436px;top:168px;width:348px;height:348px;border-radius:50%;background:#36b4ea"></div>
  <div class="abs" role="img" aria-label="Photo of a young carer and a smiling elderly woman with a walking cane" style="left:449px;top:181px;width:322px;height:322px;border-radius:50%;background:linear-gradient(135deg,#c9b3a8,#e7d7cc 45%,#b2554f 80%)"></div>

  <div class="feature l" style="left:75px;top:200px"><h3>Friendly Staff</h3><p>Lorem ipsum dolor sit amet,<br>consectetur adipiscin</p></div>
  <div class="ficon" style="left:326px;top:188px"><svg width="38" height="40" viewBox="0 0 38 40" fill="none" stroke="#fff" stroke-width="2"><circle cx="19" cy="13" r="7"/><path d="M5 38c0-9 6-14 14-14s14 5 14 14z"/></svg></div>
  <div class="feature l" style="left:75px;top:381px"><h3>Call Support 24/7</h3><p>Lorem ipsum dolor sit amet,<br>consectetur adipiscin</p></div>
  <div class="ficon" style="left:330px;top:368px"><svg width="38" height="38" viewBox="0 0 38 38" fill="none" stroke="#fff" stroke-width="2"><path d="M7 22v-5a12 12 0 0 1 24 0v5"/><rect x="5" y="20" width="6" height="10" rx="2"/><rect x="27" y="20" width="6" height="10" rx="2"/><path d="M30 30c0 4-4 5-9 5"/></svg></div>

  <div class="ficon" style="left:812px;top:186px"><svg width="40" height="36" viewBox="0 0 40 36" fill="none" stroke="#fff" stroke-width="2"><path d="M20 14c-2-4-8-3-8 1s8 9 8 9 8-5 8-9-6-5-8-1z"/><path d="M4 10v14l9 9M36 10v14l-9 9"/></svg></div>
  <div class="feature" style="left:909px;top:200px"><h3>Choice of Caregiver</h3><p>Lorem ipsum dolor sit amet,<br>consectetur adipiscin</p></div>
  <div class="ficon" style="left:812px;top:366px"><svg width="36" height="38" viewBox="0 0 36 38" fill="none" stroke="#fff" stroke-width="2"><path d="M10 34v-8a12 12 0 1 1 14-2v10"/><circle cx="18" cy="14" r="5"/></svg></div>
  <div class="feature" style="left:909px;top:381px"><h3>Peace of Mind</h3><p>Lorem ipsum dolor sit amet,<br>consectetur adipiscin</p></div>
</section>

<!-- services -->
<section class="services">
  <h2 class="section-title">OUR <b>SERVICES</b></h2>
  <span class="rule" style="left:572px;top:2021px;background:var(--blue)"></span>

  <div class="card" style="left:123px;top:2055px">
    <svg width="50" height="50" viewBox="0 0 50 50" fill="none" stroke="#0c6fb6" stroke-width="2"><path d="M6 24 25 8l19 16"/><path d="M11 20v24h28V20"/><rect x="20" y="30" width="10" height="14"/></svg>
    <h3>Light Housekeeping</h3><p>Sed ut persp iciatis unde omnis iste natus error sit voluptatem accus antium doloremque</p></div>
  <div class="card on" style="left:369px;top:2055px">
    <svg width="50" height="50" viewBox="0 0 50 50" fill="none" stroke="#fff" stroke-width="2"><circle cx="32" cy="16" r="9"/><path d="M26 22 8 40l4 4M14 34l4 4"/></svg>
    <h3>Transportation</h3><p>Sed ut persp iciatis unde omnis iste natus error sit voluptatem accus antium doloremque</p></div>
  <div class="card" style="left:615px;top:2055px">
    <svg width="50" height="50" viewBox="0 0 50 50" fill="none" stroke="#0c6fb6" stroke-width="2"><rect x="9" y="6" width="32" height="38" rx="2"/><path d="M9 14h32"/><circle cx="25" cy="29" r="9"/></svg>
    <h3>Laundry &amp; Linens</h3><p>Sed ut persp iciatis unde omnis iste natus error sit voluptatem accus antium doloremque</p></div>
  <div class="card" style="left:860px;top:2055px">
    <svg width="50" height="50" viewBox="0 0 50 50" fill="none" stroke="#0c6fb6" stroke-width="2"><rect x="12" y="4" width="18" height="7"/><rect x="9" y="11" width="24" height="32" rx="3"/><path d="M21 22v12M15 28h12"/><circle cx="38" cy="36" r="7"/></svg>
    <h3>Medication Reminders</h3><p>Sed ut persp iciatis unde omnis iste natus error sit voluptatem accus antium doloremque</p></div>

  <div class="card" style="left:123px;top:2262px">
    <svg width="50" height="50" viewBox="0 0 50 50" fill="none" stroke="#0c6fb6" stroke-width="2"><circle cx="25" cy="25" r="19"/><circle cx="25" cy="25" r="12"/></svg>
    <h3>Meal Preparation</h3><p>Sed ut persp iciatis unde omnis iste natus error sit voluptatem accus antium doloremque</p></div>
  <div class="card" style="left:369px;top:2262px">
    <svg width="50" height="50" viewBox="0 0 50 50" fill="none" stroke="#0c6fb6" stroke-width="2"><path d="M25 10a11 11 0 0 0-6 20v6h12v-6a11 11 0 0 0-6-20z"/><path d="M20 41h10M25 2v3M8 10l2 2M42 10l-2 2"/></svg>
    <h3>Stimulating Activities</h3><p>Sed ut persp iciatis unde omnis iste natus error sit voluptatem accus antium doloremque</p></div>
  <div class="card" style="left:615px;top:2262px">
    <svg width="50" height="50" viewBox="0 0 50 50" fill="none" stroke="#0c6fb6" stroke-width="2"><circle cx="12" cy="38" r="5"/><circle cx="26" cy="38" r="5"/><path d="M15 34 26 6M23 34 12 6"/><rect x="33" y="6" width="8" height="38" rx="2"/></svg>
    <h3>Hygiene Assistance</h3><p>Sed ut persp iciatis unde omnis iste natus error sit voluptatem accus antium doloremque</p></div>
  <div class="card" style="left:860px;top:2262px">
    <svg width="50" height="50" viewBox="0 0 50 50" fill="none" stroke="#0c6fb6" stroke-width="2"><path d="M4 24h42v6a10 10 0 0 1-10 10H14A10 10 0 0 1 4 30z"/><path d="M36 24V8a4 4 0 0 1 8 0"/><path d="M12 44l-2 4M38 44l2 4"/></svg>
    <h3>Kitchen &amp; Bathroom</h3><p>Sed ut persp iciatis unde omnis iste natus error sit voluptatem accus antium doloremque</p></div>
</section>

<!-- approach -->
<div class="abs approach-photo" role="img" aria-label="Photo of a carer in blue scrubs hugging an elderly man in a wheelchair in a garden"></div>
<section class="abs approach">
  <h2>SIMPLE, AFFORDABLE<br><b>APPROACH TO HOME CARE</b></h2>
  <span class="rule" style="left:84px;top:178px;background:#fff"></span>
  <p>Lorem ipsum dolor sit amet, consectetur adipiscing elit, sed do eiusmod tempor incididunt ut labore et dolore magna aliqua. Ut enim ad minim veniam, quis nostru.Lorem ipsum dolor sit amet, consectetur adipiscing elit, sed do eiusmod tempor incididunt ut labore et dolore magna aliqua.</p>
  <span class="btn" style="left:77px;top:353px;width:168px;height:44px;border:2px solid #fff">Learn more</span>
</section>

<!-- testimonials -->
<section class="quotes">
  <h2 class="section-title">WHAT <b>PEOPLE SAYS</b></h2>
  <div class="quote" style="left:161px">
    <span class="avatar" role="img" aria-label="Portrait photo of a client" style="left:163px"></span>
    <p>“Sed ut perspiciatis unde omnis iste natus error sit voluptatem accusantium doloremque laudantium, totam rem aperiam, eaque ipsa quae ab illo inventore veritatis et quasi architecto ”</p>
    <h4>Marla Quinn</h4>
  </div>
  <div class="quote" style="left:604px">
    <span class="avatar" role="img" aria-label="Portrait photo of a client" style="left:163px"></span>
    <p>“Sed ut perspiciatis unde omnis iste natus error sit voluptatem accusantium doloremque laudantium, totam rem aperiam, eaque ipsa quae ab illo inventore veritatis et quasi architecto ”</p>
    <h4>Marla Quinn</h4>
  </div>
  <div class="dots"><i></i><i class="on"></i><i></i></div>
</section>

<!-- appointment -->
<section class="abs book">
  <svg class="abs" style="left:0;top:0" width="1200" height="580" viewBox="0 0 1200 580">
    <defs><linearGradient id="bookGrad" x1="0" y1="0" x2="1" y2="1"><stop offset="0" stop-color="#0b72ba"/><stop offset=".6" stop-color="#1a8fd6"/><stop offset="1" stop-color="#0aa5e0"/></linearGradient></defs>
    <path d="M0 78Q400 20 760 18Q1000 20 1200 70V560Q800 470 420 470Q160 472 0 500Z" fill="url(#bookGrad)"/>
    <path d="M600 22Q950 -10 1200 40V70Q1000 18 600 22Z" fill="#74ab43"/>
    <path d="M0 500Q160 472 420 470Q260 480 0 530Z" fill="#74ab43"/>
  </svg>
  <h2 class="section-title">BOOK YOUR <b>APPOINTMENT</b></h2>
  <p class="sub">Flexible appointments and care options.<br><b>Call Now (555) 019 4471</b></p>
  <div class="field" style="left:165px;top:247px;width:417px;height:44px">Name</div>
  <div class="field" style="left:165px;top:303px;width:417px;height:44px">Email address</div>
  <div class="field" style="left:165px;top:361px;width:417px;height:43px">Phone Number</div>
  <div class="field" style="left:596px;top:247px;width:417px;height:157px;padding-top:10px">Message</div>
  <span class="btn" style="left:508px;top:426px;width:167px;height:44px;border:2px solid #fff">Book now</span>
</section>

<!-- footer -->
<footer>
  <div class="brand" style="left:146px;top:4236px;flex-direction:column;gap:10px">
    <span class="dot" style="width:80px;height:80px"></span>
    <span class="name" style="font-size:32px">HALVERA</span>
  </div>
  <div class="foot-col" style="left:434px"><h4>NAVIGATION</h4>About Us<br>Our Services<br>Blogs<br>Book appointment</div>
  <div class="foot-col" style="left:646px"><h4>RESOURCES</h4>Privacy Policy<br>Testimonials<br>FAQ<br>Contact Us</div>
  <div class="foot-col" style="left:838px">
    <h4>CONTACT US</h4>
    <div class="row"><span class="pin"><svg width="12" height="12" viewBox="0 0 12 12"><path fill="#fff" d="M6 0a4 4 0 0 0-4 4c0 3 4 8 4 8s4-5 4-8a4 4 0 0 0-4-4zm0 5.5A1.5 1.5 0 1 1 6 2.5a1.5 1.5 0 0 1 0 3z"/></svg></span>Location: Ferndale Springs</div>
    <div class="row"><span class="pin"><svg width="11" height="11" viewBox="0 0 24 24"><path fill="#fff" d="M6.6 10.8a15 15 0 0 0 6.6 6.6l2.2-2.2a1 1 0 0 1 1-.25 11.4 11.4 0 0 0 3.6.57 1 1 0 0 1 1 1V20a1 1 0 0 1-1 1A17 17 0 0 1 3 4a1 1 0 0 1 1-1h3.5a1 1 0 0 1 1 1c0 1.25.2 2.45.57 3.6a1 1 0 0 1-.25 1z"/></svg></span>Phone: 555-019-4471</div>
    <div style="margin-top:8px">Locally Owned, Nationally supported</div>
  </div>
  <div class="abs copy">© Copyright 2022 Halvera | All Right Reserved</div>
</footer>

</body>
</html>
```